Valve bag design

I need a valve bag for 25kg wall putty bag

Here are attached bags for reference

Most of the words or design you can copy from mablunt bag attached and company profile
Also I have attached our local product for reference

```html
<!DOCTYPE html>
<html lang="en">
<head>
<meta charset="utf-8">
<title>Crestline Wall Putty – 25kg Valve Bag</title>
<link href="https://fonts.googleapis.com/css2?family=Anton&family=Archivo:wght@700;800;900&family=Oswald:wght@400;500;600&family=Fjalla+One&display=swap" rel="stylesheet">
<style>
:root{
  --stage:#3c3d41;
  --navy:#273f6d;
  --taupe:#b2a69c;
  --white:#ffffff;
  --green:#79c824;
  --ink:#231f20;
}
*{margin:0;padding:0;box-sizing:border-box}
html,body{width:1200px;height:1200px;overflow:hidden;background:var(--stage)}
.canvas{position:relative;width:1200px;height:1200px}
.face-label{position:absolute;top:222px;width:120px;margin-left:-60px;text-align:center;color:var(--white);font-family:"Fjalla One",sans-serif;font-size:44px;line-height:1}
.panel{position:absolute;top:304px;height:628px;background:var(--white);overflow:visible}
.panel .band-top{position:absolute;left:0;top:0;width:100%;height:82px;background:var(--navy)}
.panel .rule-top{position:absolute;left:0;top:82px;width:100%;height:12px;background:var(--taupe)}
.panel .rule-bottom{position:absolute;left:0;top:573px;width:100%;height:11px;background:var(--taupe)}
.panel .band-bottom{position:absolute;left:0;top:584px;width:100%;height:44px;background:var(--navy)}
.wide{width:419px}
.narrow{width:104px}
.brand-name{position:absolute;left:0;width:100%;text-align:center;font-family:"Archivo",sans-serif;font-weight:900;color:var(--navy);letter-spacing:1px}
.wide .brand-name{top:166px;font-size:20px}
.narrow .brand-name{top:159px;font-size:10px;letter-spacing:.4px}
.net-badge{position:absolute;border-radius:50%;background:var(--green);color:var(--white);font-family:"Archivo",sans-serif;font-weight:900;text-align:center;display:flex;flex-direction:column;justify-content:center;line-height:.95}
.net-badge.large{left:333px;top:111px;width:75px;height:66px}
.net-badge.large .nw{font-size:12px}
.net-badge.large .kg{font-size:20px}
.net-badge.small{left:28px;top:508px;width:50px;height:48px}
.net-badge.small .nw{font-size:8px}
.net-badge.small .kg{font-size:13px}
.title-svg{position:absolute;overflow:visible}
.title-svg text{font-family:"Anton",sans-serif;fill:var(--navy);stroke:var(--taupe);stroke-width:2.4px;paint-order:stroke}
.wide .title-svg{left:84px;top:196px;width:290px;height:50px}
.subtitle{position:absolute;left:0;width:100%;text-align:center;font-family:"Archivo",sans-serif;font-weight:800;color:var(--ink)}
.front .subtitle{top:246px;font-size:22px}
.pitch{position:absolute;left:20px;top:284px;width:379px;text-align:center;font-family:"Archivo",sans-serif;font-weight:800;font-size:15.5px;line-height:21px;color:var(--navy)}
.features{position:absolute;left:91px;top:333px;width:232px;height:269px;background:var(--navy);border:4px solid var(--taupe)}
.features h2{position:absolute;left:11px;top:10px;font-family:"Oswald",sans-serif;font-weight:500;font-size:20px;color:var(--white);letter-spacing:-.2px}
.feature{position:absolute;left:-22px;height:28px;display:flex;align-items:center}
.feature .tick{width:24px;height:24px;flex:none}
.feature .icon{width:28px;height:27px;margin-left:8px;flex:none}
.feature span{margin-left:11px;font-family:"Oswald",sans-serif;font-size:13.5px;color:var(--white);white-space:nowrap;letter-spacing:-.2px}
.side-title{position:absolute;left:44px;top:211px;width:46px;height:272px}
.side-sub{position:absolute;left:16px;top:223px;writing-mode:vertical-rl;font-family:"Archivo",sans-serif;font-weight:800;font-size:19px;color:var(--ink);white-space:nowrap}
.back .title-svg{left:64px;top:196px}
.app-box{position:absolute;left:26px;top:255px;width:365px;height:147px;border:1.5px solid var(--navy);padding:6px 8px 0 14px;overflow:hidden}
.app-box h3{font-family:"Oswald",sans-serif;font-weight:500;font-size:11.5px;color:var(--ink);margin-bottom:3px}
.app-box ul{list-style:none}
.app-box li{position:relative;padding-left:8px;font-family:"Oswald",sans-serif;font-size:7px;line-height:9.5px;color:var(--ink)}
.app-box li::before{content:"";position:absolute;left:-2px;top:3px;width:4px;height:4px;background:var(--navy)}
.safety{position:absolute;left:26px;top:414px;width:370px;font-family:"Oswald",sans-serif;font-size:7.2px;line-height:10.6px;color:var(--ink)}
.safety b{font-weight:500;font-size:9.5px}
.spec-box{position:absolute;left:22px;top:488px;width:191px;height:66px;border:1.5px solid var(--navy);padding:4px 5px;font-family:"Oswald",sans-serif;color:var(--ink)}
.spec-box h4{font-weight:500;font-size:10.5px;line-height:13px}
.spec-row{display:flex;font-size:10px;line-height:14px;white-space:nowrap}
.spec-row .k{min-width:99px;padding-right:6px}
.distributor{position:absolute;left:236px;top:471px;width:162px;height:87px;background:var(--navy);padding:8px 10px;font-family:"Oswald",sans-serif;color:var(--white);font-size:10.5px;line-height:15.5px;white-space:nowrap}
.distributor p:first-child{font-size:11px}
</style>
</head>
<body>
<main class="canvas">
  <p class="face-label" style="left:252px">front</p>
  <p class="face-label" style="left:538px">side</p>
  <p class="face-label" style="left:820px">back</p>
  <p class="face-label" style="left:1083px">side</p>

  <!-- FRONT -->
  <section class="panel wide front" style="left:65px">
    <div class="band-top"></div><div class="rule-top"></div>
    <div class="rule-bottom"></div><div class="band-bottom"></div>
    <p class="brand-name">CRESTLINE</p>
    <div class="net-badge large"><span class="nw">Net Wt.</span><span class="kg">25kg.</span></div>
    <svg class="title-svg" viewBox="0 0 290 50"><text x="2" y="47" font-size="60" textLength="286" lengthAdjust="spacingAndGlyphs">WALL PUTTY</text></svg>
    <p class="subtitle">White Cement Based Putty</p>
    <p class="pitch">Premium wall putty to use for cement based plaster &amp; concrete surfaces before paint</p>
    <div class="features">
      <h2>The Qualities &amp; Features</h2>
      <div class="feature" style="top:48px"><svg class="tick" viewBox="0 0 24 24"><circle cx="12" cy="12" r="12" fill="#79c824"/><path d="M6 12.5l4 4 8-8.5" stroke="#fff" stroke-width="2.6" fill="none"/></svg><svg class="icon" viewBox="0 0 28 27"><rect x="1" y="1" width="26" height="25" fill="none" stroke="#fff" stroke-width="1.6"/><path d="M18 6l1.2 3.3L22 10l-2.8 1L18 14l-1.2-3L14 10l2.8-.7z M9 15l.7 1.8 1.8.7-1.8.7L9 20l-.7-1.8-1.8-.7 1.8-.7z" fill="#fff"/></svg><span>Very smooth and glossy finish.</span></div>
      <div class="feature" style="top:77px"><svg class="tick" viewBox="0 0 24 24"><circle cx="12" cy="12" r="12" fill="#79c824"/><path d="M6 12.5l4 4 8-8.5" stroke="#fff" stroke-width="2.6" fill="none"/></svg><svg class="icon" viewBox="0 0 28 27"><rect x="1" y="1" width="26" height="25" fill="none" stroke="#fff" stroke-width="1.6"/><path d="M5 10q8 2 18-3M8 13l5 8 2-3 3 3" stroke="#fff" stroke-width="1.4" fill="none"/></svg><span>Suitable for all cement surfaces.</span></div>
      <div class="feature" style="top:107px"><svg class="tick" viewBox="0 0 24 24"><circle cx="12" cy="12" r="12" fill="#79c824"/><path d="M6 12.5l4 4 8-8.5" stroke="#fff" stroke-width="2.6" fill="none"/></svg><svg class="icon" viewBox="0 0 28 27"><rect x="1" y="1" width="26" height="25" fill="none" stroke="#fff" stroke-width="1.6"/><path d="M5 13L14 5l9 8M8 11v11h12V11" stroke="#fff" stroke-width="1.6" fill="none"/><circle cx="14" cy="16" r="3" stroke="#fff" fill="none"/></svg><span>Suitable for Interior &amp; exterior.</span></div>
      <div class="feature" style="top:136px"><svg class="tick" viewBox="0 0 24 24"><circle cx="12" cy="12" r="12" fill="#79c824"/><path d="M6 12.5l4 4 8-8.5" stroke="#fff" stroke-width="2.6" fill="none"/></svg><svg class="icon" viewBox="0 0 28 27"><rect x="1" y="1" width="26" height="25" fill="none" stroke="#fff" stroke-width="1.6"/><path d="M5 9h18M5 18h18M14 4v4M14 19v4M8 11l12 5M8 14l12 2" stroke="#fff" stroke-width="1.3"/></svg><span>Very high tensile adhesion.</span></div>
      <div class="feature" style="top:166px"><svg class="tick" viewBox="0 0 24 24"><circle cx="12" cy="12" r="12" fill="#79c824"/><path d="M6 12.5l4 4 8-8.5" stroke="#fff" stroke-width="2.6" fill="none"/></svg><svg class="icon" viewBox="0 0 28 27"><rect x="1" y="1" width="26" height="25" fill="none" stroke="#fff" stroke-width="1.6"/><path d="M8 7q-3 5 0 6q3-1 0-6zM14 6q-3 5 0 6q3-1 0-6zM20 7q-3 5 0 6q3-1 0-6z" fill="#fff"/><rect x="4" y="16" width="20" height="6" fill="#fff"/></svg><span>Very low water absorption.</span></div>
      <div class="feature" style="top:195px"><svg class="tick" viewBox="0 0 24 24"><circle cx="12" cy="12" r="12" fill="#79c824"/><path d="M6 12.5l4 4 8-8.5" stroke="#fff" stroke-width="2.6" fill="none"/></svg><svg class="icon" viewBox="0 0 28 27"><rect x="1" y="1" width="26" height="25" fill="none" stroke="#fff" stroke-width="1.6"/><path d="M11 5q-6 9-2 13q4-1 2-13zM17 9q-4 6-1 9q3-1 1-9z" fill="#fff"/><circle cx="20" cy="19" r="3.5" fill="#fff"/></svg><span>No water curring needed.</span></div>
      <div class="feature" style="top:225px"><svg class="tick" viewBox="0 0 24 24"><circle cx="12" cy="12" r="12" fill="#79c824"/><path d="M6 12.5l4 4 8-8.5" stroke="#fff" stroke-width="2.6" fill="none"/></svg><svg class="icon" viewBox="0 0 28 27"><rect x="1" y="1" width="26" height="25" fill="none" stroke="#fff" stroke-width="1.6"/><path d="M5 5h14v10M8 10l10 10M13 20h6v-6" stroke="#fff" stroke-width="1.5" fill="none"/></svg><span>Very high coverage and easy to apply.</span></div>
    </div>
  </section>

  <!-- SIDE -->
  <section class="panel narrow side" style="left:492px">
    <div class="band-top"></div><div class="rule-top"></div>
    <div class="rule-bottom"></div><div class="band-bottom"></div>
    <p class="brand-name">CRESTLINE</p>
    <svg class="title-svg side-title" viewBox="0 0 46 272"><text transform="translate(2,0) rotate(90)" x="0" y="0" font-size="58" textLength="270" lengthAdjust="spacingAndGlyphs">WALL PUTTY</text></svg>
    <p class="side-sub">White Cement Based Putty</p>
    <div class="net-badge small"><span class="nw">Net Wt.</span><span class="kg">25kg.</span></div>
  </section>

  <!-- BACK -->
  <section class="panel wide back" style="left:606px">
    <div class="band-top"></div><div class="rule-top"></div>
    <div class="rule-bottom"></div><div class="band-bottom"></div>
    <p class="brand-name">CRESTLINE</p>
    <svg class="title-svg" viewBox="0 0 290 50"><text x="2" y="47" font-size="60" textLength="286" lengthAdjust="spacingAndGlyphs">WALL PUTTY</text></svg>
    <div class="app-box">
      <h3>APPLICATION RECOMMENDATIONS</h3>
      <ul>
        <li>Apply on cement / concrete cement plaster surfaces, wallboard and gypsum/plaster board.<br>25kg. of Crestline Wall Putty added to approximately 8.5 - 10 liters of clean water, mixing may be done manually or by using a suitable electric mixer.</li>
        <li>Prepared mortar is left to mature for 4 - 8 minutes and mixed again before use. the mortar must be used in 2 - 3 hours<br>Remove all dust, loose articles from the surface, oil, paint, curing agent, lime and silicones before application of Crestline Wall Putty</li>
        <li>Ensure that the surface is moisturized before the application, cracks and holes must be repaired with appropriate mortar.</li>
        <li>Apply 1st coat of Crestline Wall Putty (1.5mm thickness) using a blade/spatula on the wall with a bottom to up configuration</li>
        <li>Apply 2nd coat of Crestline Wall Putty (1.0mm thickness) preferably after 4 hours during summers and after 12 hours during winters, second coat shall be applied horizontally to even out application marks of 1st coat, if any.</li>
        <li>Consumption Approximately 1kg/m2 (for 1mm thickness)<br>Shelf life unopened bag can be stored in dry environment for up to 12 month stacked maximum 12 packages on a place</li>
      </ul>
    </div>
    <p class="safety"><b>Health and Safety:</b> Avoid contact with food, skin, eyes, and mouth during usage and strong use rubber gloves while mixing take precautions to avoid dust infection while handling putty powdered by wearing nose mask, if swallowed by accident consult a doctor Rinse with plenty of water in case of contact with skin.<br>KEEP OUT OF REACH OF CHILDREN</p>
    <div class="spec-box">
      <h4>PRODUCT SPECIFICATIONS</h4>
      <div class="spec-row"><span class="k">Compressive Strength</span><span>28 day-14 N /mm</span></div>
      <div class="spec-row"><span class="k">Adhesion Strength</span><span>28 day-238 N /mm</span></div>
      <div class="spec-row"><span class="k">Water requirement by volume</span><span>38%</span></div>
    </div>
    <div class="distributor">
      <p>MARKETED AND DISTRIBUTED BY:</p>
      <p>HARBANOW BUILDING LTD.</p>
      <p>Tel: +000 700 123 456</p>
      <p>info@harbanowbuilding.com</p>
      <p style="line-height:11px">harbanowbuilding.com</p>
    </div>
  </section>

  <!-- SIDE -->
  <section class="panel narrow side" style="left:1031px">
    <div class="band-top"></div><div class="rule-top"></div>
    <div class="rule-bottom"></div><div class="band-bottom"></div>
    <p class="brand-name">CRESTLINE</p>
    <svg class="title-svg side-title" viewBox="0 0 46 272"><text transform="translate(2,0) rotate(90)" x="0" y="0" font-size="58" textLength="270" lengthAdjust="spacingAndGlyphs">WALL PUTTY</text></svg>
    <p class="side-sub">White Cement Based Putty</p>
    <div class="net-badge small"><span class="nw">Net Wt.</span><span class="kg">25kg.</span></div>
  </section>
</main>
</body>
</html>
```